Vow Lanterns - Outdoor Ceremony Designs

We set up wedding ceremonies outside in parks in and beaches. The advert will be in magazines. The design needs to look trendy but sophisticated and show a range of our products in different locations. Here is our website if you need any idea's www.vowlanterns.com.au please ask questions.

Target Market(s)

Females ages 25 to 35

Industry/Entity Type

Wedding

Requirements
Must have
• Spec for the magazine that the ad will be going into:
• HALF PAGE (LANDSCAPE):
• 284MM X 95MM (Width x Height) NO BLEED
• SUPPLY
• ARTWORK SPECIFICATIONS
• SUBMITTING YOUR ARTWORK
• If you are providing us with your own artwork, it is your responsibility to make sure it is set up correctly and to all our required specifications. If it is not, you may be charged an additional fee. We have the right to refuse your artwork if it does not reflect the quality standard of our brochure.
• YOU CAN SEND YOUR ARTWORK VIA CD/DVD OR EMAIL
• ARTWORK SPECIFICATIONS
• Please supply a Commercial Print Ready PDF or JPEG document only.
• IMAGES: All images used in your artwork must be a resolution of 300dpi or above 1mb. Below this will not be accepted.
• FONTS: All fonts must be outlined and embedded. No fonts should go below 8pt for visibility purposes.
• COLOURS: CMYK not RGB. Please remove all spot colours; we will not accept artwork with spot colours.
• BLEED: Only required for a full page advertisement, no bleed is required on any of the other advertisement artwork sizes.
• If any changes need to be made to the clients existing artwork there maybe an additional fee charged and will be on a case by case basis. Please note that working art files will be required, for example a packaged idml or eps with fonts supplied.
• ADVERTISEMENT SELECTION
• 3. HALF PAGE (LANDSCAPE):
• BLEED IS ONLY REQUIRED FOR THE FULL PAGE, NO BLEED IS REQUIRED ON THE OTHER ADVERTISEMENT ARTWORK.
Nice to have
• Outdoor Ceremony Designs - Ph: 0472 318 694
• www.vowlanterns.com.au

```html
<!DOCTYPE html>
<html lang="en">
<head>
<meta charset="utf-8">
<title>Vow Lanterns – Outdoor Ceremony Designs</title>
<link rel="stylesheet" href="https://fonts.googleapis.com/css2?family=Marcellus&family=Quicksand:wght@500&display=swap">
<style>
  :root {
    --stage: #000000;
    --olive: #a8b43c;
    --olive-deep: #8f9f33;
    --teal: #3a8a92;
    --teal-bright: #2fd6c4;
    --cyan: #27c4ee;
    --leaf: #4fd66e;
    --sun: #f2c531;
    --amber: #e69a1c;
    --ink: #151515;
    --white: #ffffff;
  }
  * { margin: 0; padding: 0; box-sizing: border-box; }
  html, body { width: 1200px; height: 600px; overflow: hidden; background: var(--stage); }
  .canvas { position: relative; width: 1200px; height: 600px; background: var(--stage); }
  .banner-art { position: absolute; left: 0; top: 0; }
  .brand-block {
    position: absolute; left: 400px; top: 100px; width: 380px; height: 397px;
    text-align: center; color: var(--white);
  }
  .tagline {
    position: absolute; top: 18px; width: 100%;
    font: 500 19px/1 "Quicksand", sans-serif; letter-spacing: 0.3px;
  }
  .brand-name {
    position: absolute; top: 82px; width: 100%;
    font: 400 66px/1.05 "Marcellus", serif; color: var(--ink);
  }
  .divider {
    position: absolute; top: 287px; left: 42px; width: 350px; height: 1px;
    background: rgba(255,255,255,0.7);
  }
  .service {
    position: absolute; top: 298px; width: 100%;
    font: 400 29px/1 "Marcellus", serif;
  }
  .contact {
    position: absolute; top: 338px; width: 100%;
    font: 500 16px/1.3 "Quicksand", sans-serif;
  }
</style>
</head>
<body>
<div class="canvas">
  <svg class="banner-art" width="1200" height="600" viewBox="0 0 1200 600" xmlns="http://www.w3.org/2000/svg">
    <defs>
      <linearGradient id="beachTone" x1="0" y1="0" x2="0" y2="1">
        <stop offset="0" stop-color="#6f9fd6"/>
        <stop offset="0.42" stop-color="#cfe0f2"/>
        <stop offset="0.5" stop-color="#2aa6a8"/>
        <stop offset="0.6" stop-color="#eef2f4"/>
        <stop offset="1" stop-color="#d8d8dc"/>
      </linearGradient>
      <linearGradient id="lawnTone" x1="0" y1="0" x2="0" y2="1">
        <stop offset="0" stop-color="#3f5a2a"/>
        <stop offset="0.45" stop-color="#dcdcd0"/>
        <stop offset="1" stop-color="#6aa53a"/>
      </linearGradient>
      <linearGradient id="gardenTone" x1="0" y1="0" x2="0" y2="1">
        <stop offset="0" stop-color="#5d6f3a"/>
        <stop offset="0.4" stop-color="#9a7a80"/>
        <stop offset="0.6" stop-color="#e6e6e0"/>
        <stop offset="1" stop-color="#5fa236"/>
      </linearGradient>
      <linearGradient id="panelTone" x1="0" y1="0" x2="1" y2="0">
        <stop offset="0" stop-color="#3c8790"/>
        <stop offset="0.45" stop-color="#8fae52"/>
        <stop offset="0.7" stop-color="#a8b43c"/>
        <stop offset="1" stop-color="#a8b43c"/>
      </linearGradient>
      <linearGradient id="baseLine" x1="0" y1="0" x2="1" y2="0">
        <stop offset="0" stop-color="#c8d84a"/>
        <stop offset="0.35" stop-color="#e0b22a"/>
        <stop offset="0.7" stop-color="#d7e04a"/>
        <stop offset="1" stop-color="#4fbf3a"/>
      </linearGradient>
    </defs>

    <g class="photo-beach" role="img" aria-label="Photo: beach wedding aisle with white chairs and a draped bamboo arch by the sea">
      <rect x="0" y="100" width="460" height="397" fill="url(#beachTone)"/>
    </g>

    <g class="accent-shards">
      <polygon points="150,100 300,100 385,280" fill="var(--cyan)" opacity="0.7"/>
      <polygon points="255,100 445,100 385,280" fill="var(--leaf)" opacity="0.75"/>
      <polygon points="255,215 385,280 350,330" fill="var(--sun)" opacity="0.7"/>
      <polygon points="350,330 385,280 372,400" fill="var(--sun)" opacity="0.45"/>
    </g>

    <g class="photo-lawn" role="img" aria-label="Photo: rows of white chairs with ribbons on a sunny garden lawn">
      <polygon points="900,100 1200,100 1200,298 848,298" fill="url(#lawnTone)"/>
    </g>
    <g class="photo-garden" role="img" aria-label="Photo: garden ceremony with white aisle runner, pedestals and floral arch">
      <polygon points="848,298 1200,298 1200,497 788,497" fill="url(#gardenTone)"/>
    </g>

    <polygon class="edge-teal" points="903,100 918,100 862,298 846,298" fill="var(--teal-bright)"/>
    <polygon class="edge-amber" points="846,298 862,298 803,497 787,497" fill="var(--amber)"/>

    <polygon class="edge-left" points="428,100 446,100 342,497 322,497" fill="var(--teal)"/>
    <polygon class="brand-panel" points="446,100 903,100 787,497 342,497" fill="url(#panelTone)"/>

    <rect class="base-line" x="0" y="493" width="1200" height="4" fill="url(#baseLine)"/>
  </svg>

  <div class="brand-block">
    <p class="tagline">Your awesome tagline goes here!!</p>
    <h1 class="brand-name">Vow<br>Lanterns</h1>
    <div class="divider"></div>
    <p class="service">Outdoor Ceremony Designs</p>
    <p class="contact">Call us | 0472 318 694<br>www.vowlanterns.com.au</p>
  </div>
</div>
</body>
</html>
```